office stationary for pr
pr biz stationery
Creative Brief
Simple
Adaeze Nnorom
14 mabel close eastern lagoonview estate off harmon drive lekki lagos
annorom@pelvora.com
www.pelvora.com
the logo should be used at the back of the business card

```html
<!DOCTYPE html>
<html lang="en">
<head>
<meta charset="utf-8">
<title>Pelvora Stationery</title>
<link rel="stylesheet" href="https://fonts.googleapis.com/css2?family=Cormorant+Garamond:wght@400;500&display=swap">
<style>
:root{
  --stage:#1c2330;
  --paper:#ffffff;
  --slate:#48627f;
  --slate-deep:#3d5572;
  --sky:#8fb6d3;
  --sky-pale:#e4eef6;
  --ink:#4a4f58;
  --rule:#b9c3cd;
}
*{margin:0;padding:0;box-sizing:border-box}
html,body{width:1200px;height:901px;overflow:hidden;background:var(--stage)}
body{position:relative;font-family:"Cormorant Garamond",Georgia,serif;color:var(--ink)}
.piece{position:absolute;background:var(--paper);overflow:hidden}
.motif{position:absolute}
.brand{position:absolute;font-family:"Cormorant Garamond",Georgia,serif;font-weight:400;color:var(--sky);line-height:1;display:flex;align-items:center;gap:6px;white-space:nowrap}
.brand .dot{width:7px;height:7px;border-radius:50%;background:var(--sky)}
.rule{position:absolute;height:1px;background:var(--rule)}
.address{position:absolute;font-size:8px;line-height:1.25;text-align:right;color:var(--ink)}
.strip{position:absolute;top:0;bottom:0;background:var(--slate)}
.strip-url{position:absolute;color:#dfe8f1;font-size:8px;transform:rotate(90deg);transform-origin:left top;white-space:nowrap}

/* envelopes */
.envelope-a{left:37px;top:29px;width:571px;height:190px}
.envelope-b{left:628px;top:29px;width:548px;height:190px}

/* cards */
.card{position:absolute;left:68px;width:171px;overflow:hidden}
.card-front{background:var(--paper)}
.card-back{background:var(--slate-deep)}
.card-name{position:absolute;left:12px;top:12px;font-size:7px;font-weight:500;letter-spacing:.3px;color:var(--ink)}
.card-title{position:absolute;left:12px;top:22px;font-size:5.5px;color:var(--sky)}
.card-lines{position:absolute;left:12px;top:38px;font-size:5px;line-height:1.45;color:var(--ink)}

/* letterhead */
.letterhead{left:273px;top:263px;width:428px;height:618px}
.letter-body{position:absolute;left:38px;top:128px;width:330px;font-size:5.6px;line-height:1.55;color:var(--ink)}
.letter-body p{margin-bottom:9px}
.letter-date{margin-bottom:12px!important}

/* folder */
.folder{position:absolute;left:733px;top:263px;width:443px;height:618px;background:var(--slate);overflow:hidden}
</style>
</head>
<body>

<!-- Envelope A -->
<section class="piece envelope-a">
  <svg class="motif" style="left:0;top:40px" width="260" height="150" role="img" aria-label="Faint leaf motif">
    <defs><radialGradient id="leafA" cx="30%" cy="80%" r="70%"><stop offset="0" stop-color="#d7e6f1"/><stop offset="1" stop-color="#ffffff"/></radialGradient></defs>
    <rect width="260" height="150" fill="url(#leafA)"/>
  </svg>
  <div class="brand" style="left:28px;top:28px;font-size:34px">pelvora<span class="dot"></span></div>
  <div class="rule" style="left:150px;top:52px;width:270px"></div>
  <div class="address" style="left:390px;top:60px;width:150px">14 mabel close<br>eastern lagoonview estate<br>off harmon drive<br>lekki lagos</div>
  <div class="strip" style="left:542px;width:29px"></div>
</section>

<!-- Envelope B -->
<section class="piece envelope-b">
  <svg class="motif" style="left:0;top:40px" width="240" height="150" role="img" aria-label="Faint leaf motif">
    <defs><radialGradient id="leafB" cx="35%" cy="85%" r="70%"><stop offset="0" stop-color="#dbe8f2"/><stop offset="1" stop-color="#ffffff"/></radialGradient></defs>
    <rect width="240" height="150" fill="url(#leafB)"/>
  </svg>
  <div class="brand" style="left:42px;top:28px;font-size:34px">pelvora<span class="dot"></span></div>
  <div class="rule" style="left:170px;top:52px;width:330px"></div>
  <div class="rule" style="left:20px;top:158px;width:480px"></div>
  <div class="address" style="left:20px;top:162px;width:400px;text-align:left">14 mabel close eastern lagoonview estate off harmon drive lekki lagos</div>
  <div class="strip" style="left:516px;width:32px"></div>
  <div class="strip-url" style="left:536px;top:40px">www.pelvora.com</div>
</section>

<!-- Business cards -->
<article class="card card-front" style="top:329px;height:104px">
  <div class="card-name">Adaeze Nnorom</div>
  <div class="card-title">Director</div>
  <div class="card-lines">+234 801 234 5678<br>annorom@pelvora.com<br>www.pelvora.com<br>14 mabel close, lekki lagos</div>
  <div class="brand" style="left:100px;top:42px;font-size:16px">pelvora</div>
</article>
<article class="card card-back" style="top:443px;height:97px">
  <div class="brand" style="left:50px;top:38px;font-size:22px;color:#dfe8f1">pelvora</div>
</article>
<article class="card card-front" style="top:555px;height:97px">
  <div class="card-name">Adaeze Nnorom</div>
  <div class="card-title">Director</div>
  <div class="card-lines">+234 801 234 5678<br>annorom@pelvora.com<br>www.pelvora.com<br>14 mabel close, lekki lagos</div>
  <div class="brand" style="left:100px;top:40px;font-size:16px">pelvora</div>
</article>
<article class="card card-back" style="top:669px;height:98px">
  <div class="brand" style="left:50px;top:38px;font-size:22px;color:#dfe8f1">pelvora</div>
</article>

<!-- Letterhead -->
<section class="piece letterhead">
  <svg class="motif" style="left:0;top:400px" width="260" height="218" role="img" aria-label="Faint leaf motif">
    <defs><radialGradient id="leafL" cx="25%" cy="85%" r="75%"><stop offset="0" stop-color="#dae7f1"/><stop offset="1" stop-color="#ffffff"/></radialGradient></defs>
    <rect width="260" height="218" fill="url(#leafL)"/>
  </svg>
  <div class="brand" style="left:22px;top:24px;font-size:30px">pelvora<span class="dot"></span></div>
  <div class="rule" style="left:140px;top:46px;width:260px"></div>
  <div class="letter-body">
    <p class="letter-date">March 22, 2011</p>
    <p>Thank you for meeting with us last week. We are pleased to share our proposal for the coming season and look forward to building a strong and lasting partnership with your team across every channel we discussed together.</p>
    <p>Our approach keeps the message simple and clear. Each release is planned with care, shared with the right press contacts and followed up closely so that your story reaches the people who matter most.</p>
    <p>Please review the attached schedule and let us know of any changes. We will gladly adjust the plan to suit your goals.</p>
    <p>Kind regards to you and your team.</p>
    <p style="margin-top:14px">Sincerely yours,</p>
    <p style="margin-top:14px">Adaeze Nnorom</p>
  </div>
  <div class="address" style="left:250px;top:540px;width:150px">14 mabel close<br>eastern lagoonview estate<br>off harmon drive<br>lekki lagos<br>www.pelvora.com</div>
</section>

<!-- Folder -->
<section class="folder">
  <svg class="motif" style="left:0;top:330px" width="300" height="288" role="img" aria-label="Faint leaf motif">
    <defs><radialGradient id="leafF" cx="30%" cy="85%" r="75%"><stop offset="0" stop-color="#6c88a6"/><stop offset="1" stop-color="#48627f"/></radialGradient></defs>
    <rect width="300" height="288" fill="url(#leafF)"/>
  </svg>
  <div class="rule" style="left:30px;top:262px;width:380px;background:#8aa3bd"></div>
  <div class="brand" style="left:140px;top:232px;font-size:56px;color:#e3ecf4;background:var(--slate);padding:0 10px">pelvora</div>
</section>

</body>
</html>
```